owlbrass website

commerce website to sell cookeries, brackets, mailboxes and to show off homes built. Modern Steel in design see tandra wheels web page to be like: https://www.tandrawheels.example/en/ sorry its net haven hosting word press divi

must be able to add products to page

Target Market(s)

mainly western states of U.S.

Industry/Entity Type

Building Product

Coding

Coded - Design and coding required

Number of Pages Required

3 page

Font styles to use
Sans Serif

Colors

Designer to choose colors to be used in the design.

Requirements
Must have
• customers to be able to order products from page
• net haven hosting word press divi

```html
<!DOCTYPE html>
<html lang="en">
<head>
<meta charset="utf-8">
<title>Owlbrass — Products</title>
<link href="https://fonts.googleapis.com/css2?family=Poppins:wght@400;500;600&family=Roboto:wght@400;500;700&display=swap" rel="stylesheet">
<style>
:root{
  --brand:#40608e;
  --brand-dark:#36527c;
  --accent:#4a78c0;
  --page:#f3f3f3;
  --card:#ffffff;
  --ink:#222;
  --muted:#555;
  --star:#f3a225;
  --line:#d9d9d9;
}
*{box-sizing:border-box;margin:0;padding:0}
html,body{width:1200px;height:2243px;overflow:hidden}
body{font-family:"Roboto",sans-serif;background:var(--page);color:var(--ink);position:relative}
a{color:inherit;text-decoration:none}

/* header */
.site-header{position:absolute;left:0;top:0;width:1200px;height:122px;background:var(--brand);color:#fff}
.brand{position:absolute;left:87px;top:40px;display:flex;align-items:center;gap:10px;font-family:"Poppins",sans-serif;font-size:24px;font-weight:500;letter-spacing:1px}
.brand-dot{width:16px;height:16px;border-radius:50%;background:#fff}
.main-nav{position:absolute;left:333px;top:21px;display:flex;gap:26px;font-size:14px}
.top-links{position:absolute;right:89px;top:23px;font-size:12.5px}
.search-bar{position:absolute;left:335px;top:59px;width:431px;height:36px;background:#fff;display:flex;align-items:center}
.search-bar .scope{width:43px;height:100%;border-right:1px solid var(--line);font-size:11px;color:#555;display:flex;align-items:center;justify-content:center;font-weight:500}
.search-bar .field{flex:1;padding-left:18px;font-size:11.5px;color:#666}
.search-bar .go{width:49px;height:100%;background:var(--accent);display:flex;align-items:center;justify-content:center}
.account-tools{position:absolute;left:785px;top:62px;display:flex;gap:16px;font-size:12.5px;line-height:14px}
.tool{display:flex;align-items:center;gap:8px}
.tool small{display:block;font-size:11px;opacity:.9}

/* title bar */
.title-bar{position:absolute;left:0;top:122px;width:1200px;height:62px;background:#fff;display:flex;align-items:center;justify-content:space-between;padding:0 89px}
.title-bar h1{font-family:"Poppins",sans-serif;font-size:17px;font-weight:600;letter-spacing:.5px}
.crumbs{font-size:14px}

/* sidebar */
.sidebar{position:absolute;left:89px;top:222px;width:230px;height:767px;background:#fff;border-radius:6px;font-family:"Poppins",sans-serif}
.sidebar .block{position:absolute;left:20px;width:190px}
.sidebar h2{position:absolute;left:20px;font-size:17px;font-weight:400;line-height:20px;letter-spacing:.3px}
.store-search{display:flex;height:37px}
.store-search span{flex:1;background:#f1f1f1;font-size:12px;color:#555;display:flex;align-items:center;padding-left:13px}
.store-search i{width:37px;background:var(--accent);display:flex;align-items:center;justify-content:center}
.facet{list-style:none;font-size:13.5px;color:#444}
.facet li{display:flex;justify-content:space-between;align-items:center;height:24px}
.facet .box{display:inline-block;width:14px;height:14px;border:1px solid #bbb;margin-right:12px;vertical-align:-2px}
.divider{position:absolute;left:16px;width:198px;border:0;border-top:1px solid var(--line)}
.swatches{display:grid;grid-template-columns:repeat(5,34px);grid-auto-rows:32px;gap:3px;margin-left:2px}

.promo{position:absolute;left:89px;top:1007px;width:230px;height:286px;border-radius:6px;overflow:hidden;background:linear-gradient(160deg,#ececec 0%,#d7d2cb 45%,#9aa0a8 100%)}
.promo p{position:absolute;left:0;width:100%;text-align:center;font-family:"Poppins",sans-serif}
.promo .kicker{top:48px;font-size:14px;font-weight:500}
.promo .headline{top:62px;font-size:23px;font-weight:600;letter-spacing:.3px}

/* products */
.listing-bar{position:absolute;left:346px;top:219px;width:764px;height:32px;display:flex;align-items:center;font-size:13px;color:#555}
.listing-bar .views{display:flex;gap:8px;margin-right:14px}
.sort{margin-left:auto;display:flex;align-items:center;gap:8px}
.sort .select{width:177px;height:32px;background:#fff;border:1px solid #e6e6e6;display:flex;align-items:center;justify-content:space-between;padding:0 10px;color:#333}
.grid{position:absolute;left:346px;top:270px;width:764px;display:grid;grid-template-columns:repeat(3,246px);column-gap:13px;row-gap:18px}
.card{height:348px;background:var(--card);border-radius:6px;position:relative;text-align:center}
.card .photo{position:absolute;left:38px;top:36px;width:170px;height:140px;border-radius:4px}
.card h3{position:absolute;top:196px;left:0;width:100%;font-size:18px;font-weight:500;line-height:18px;color:#333}
.card .price{position:absolute;top:240px;left:0;width:100%;font-size:14px;font-weight:500}
.card .price b{color:var(--accent);font-size:17px;font-weight:700}
.card .stars{position:absolute;top:262px;left:0;width:100%;color:var(--star);font-size:15px;letter-spacing:3px}
.card .actions{position:absolute;top:282px;left:0;width:100%;display:flex;justify-content:center;gap:9px}
.wish{width:31px;height:31px;background:#e4e4e4;display:flex;align-items:center;justify-content:center}
.cart{width:108px;height:32px;border:2px solid var(--brand);color:var(--brand);font-size:12px;font-weight:700;display:flex;align-items:center;justify-content:center}

.pager{position:absolute;left:571px;top:1760px;display:flex;align-items:center;font-size:12px;color:#333}
.pager .prev{width:76px;height:30px;border-radius:15px;background:#e8e8e8;display:flex;align-items:center;justify-content:center;margin-right:18px}
.pager .num{width:26px;text-align:center}
.pager .current{width:30px;height:30px;border-radius:50%;background:#222;color:#fff;display:flex;align-items:center;justify-content:center;margin:0 4px}
.pager .next{width:77px;height:30px;border-radius:15px;background:var(--accent);color:#fff;display:flex;align-items:center;justify-content:center;margin-left:24px}

/* footer */
.site-footer{position:absolute;left:0;top:1869px;width:1200px;height:374px;background:var(--brand);color:#fff}
.footer-brand{position:absolute;left:96px;top:160px;width:228px;text-align:center}
.footer-brand .name{display:flex;align-items:center;justify-content:center;gap:10px;font-family:"Poppins",sans-serif;font-size:32px;font-weight:500;letter-spacing:1px}
.footer-brand .name span{width:20px;height:20px;border-radius:50%;background:#fff}
.footer-brand p{margin-top:14px;font-size:12.5px;line-height:19px}
.col{position:absolute;top:94px}
.col h4{font-size:16px;font-weight:500;margin-bottom:12px;letter-spacing:.2px}
.col li{list-style:none;font-size:14.5px;height:25px;padding-left:4px}
.contact li{display:flex;gap:8px;font-size:13.5px;height:auto;margin-bottom:9px;line-height:20px;padding-left:0}
.social{display:flex;gap:13px;margin-top:6px}
.social span{width:10px;height:10px;border-radius:50%;background:#fff}
.footer-rule{position:absolute;left:89px;top:318px;width:1022px;border-top:1px solid rgba(255,255,255,.2)}
.copyright{position:absolute;left:89px;top:341px;font-size:13.5px;font-weight:500}
.legal{position:absolute;right:89px;top:341px;font-size:13.5px;font-weight:500}
.to-top{position:absolute;left:1137px;top:306px;width:34px;height:34px;border-radius:50%;background:#fff;display:flex;align-items:center;justify-content:center}
</style>
</head>
<body>

<header class="site-header">
  <div class="brand"><span class="brand-dot"></span>OWLBRASS</div>
  <nav class="main-nav"><a>Today's Deals</a><a>Help</a><a>Registry</a><a>Gift Cards</a><a>Sell</a></nav>
  <div class="top-links">One Request, Multiple Quotes &nbsp;|&nbsp; Shop Today's Deals</div>
  <div class="search-bar">
    <div class="scope">ALL</div>
    <div class="field">Search for Products, Brands and More</div>
    <div class="go"><svg width="15" height="15" viewBox="0 0 16 16" fill="none" stroke="#fff" stroke-width="1.8"><circle cx="7" cy="7" r="5"/><path d="M11 11l4 4"/></svg></div>
  </div>
  <div class="account-tools">
    <div class="tool"><svg width="26" height="28" viewBox="0 0 26 28" fill="none" stroke="#fff" stroke-width="1.8"><circle cx="13" cy="9" r="6"/><path d="M2 27c0-6 5-10 11-10s11 4 11 10"/></svg><div><small>Sign In Join Free</small>Owlbrass</div></div>
    <div class="tool"><svg width="24" height="28" viewBox="0 0 24 28" fill="none" stroke="#fff" stroke-width="1.8"><rect x="2" y="8" width="20" height="18"/><path d="M7 8V5a5 5 0 0110 0v3"/></svg><div>Order<br>Protection</div></div>
    <div class="tool"><svg width="30" height="26" viewBox="0 0 30 26" fill="none" stroke="#fff" stroke-width="1.8"><path d="M15 24S2 16 2 8a6.5 6.5 0 0113-1 6.5 6.5 0 0113 1c0 8-13 16-13 16z"/></svg><div>0<br>Favorites</div></div>
  </div>
</header>

<div class="title-bar"><h1>PRODUCTS</h1><div class="crumbs">Home / Products</div></div>

<aside class="sidebar">
  <h2 style="top:27px">SEARCH</h2>
  <div class="block store-search" style="top:55px"><span>Search Our Store</span><i><svg width="15" height="15" viewBox="0 0 16 16" fill="none" stroke="#fff" stroke-width="1.8"><circle cx="7" cy="7" r="5"/><path d="M11 11l4 4"/></svg></i></div>

  <h2 style="top:115px">CATEGORIES</h2>
  <ul class="block facet" style="top:141px"><li>Accessories<span>(15)</span></li><li>Featured Product<span>(17)</span></li><li>New Products<span>(16)</span></li></ul>
  <hr class="divider" style="top:234px">

  <h2 style="top:259px">VENDORS</h2>
  <ul class="block facet" style="top:288px">
    <li><span><i class="box"></i>Vendor 1</span></li>
    <li><span><i class="box"></i>Vendor 10</span></li>
    <li><span><i class="box"></i>Vendor 11</span></li>
    <li><span><i class="box"></i>Vendor 2</span></li>
    <li><span><i class="box"></i>Vendor 3</span></li>
  </ul>
  <hr class="divider" style="top:435px">

  <h2 style="top:460px">COLOR</h2>
  <div class="block swatches" style="top:491px">
    <span style="background:#cfcfcf"></span><span style="background:#dadada"></span><span style="background:#b0b0b0"></span><span style="background:#c2c2c2"></span><span style="background:#9a9a9a"></span>
    <span style="background:#8a8a8a"></span><span style="background:#707070"></span><span style="background:#808080"></span><span style="background:#666"></span><span style="background:#3b3b3b"></span>
  </div>
  <hr class="divider" style="top:591px">

  <h2 style="top:616px">SIZE</h2>
  <ul class="block facet" style="top:643px">
    <li><span><i class="box"></i>S</span><span>(4)</span></li>
    <li><span><i class="box"></i>M</span><span>(5)</span></li>
    <li><span><i class="box"></i>L</span><span>(7)</span></li>
    <li><span><i class="box"></i>XL</span><span>(3)</span></li>
  </ul>
</aside>

<div class="promo" role="img" aria-label="Photo of a woman and child cooking together in a bright kitchen">
  <p class="kicker">SALE UP TO 50% OFF</p>
  <p class="headline">DINNING WARE</p>
</div>

<div class="listing-bar">
  <div class="views">
    <svg width="16" height="16" viewBox="0 0 16 16" fill="#4a78c0"><rect x="0" y="0" width="4" height="4"/><rect x="6" y="0" width="4" height="4"/><rect x="12" y="0" width="4" height="4"/><rect x="0" y="6" width="4" height="4"/><rect x="6" y="6" width="4" height="4"/><rect x="12" y="6" width="4" height="4"/><rect x="0" y="12" width="4" height="4"/><rect x="6" y="12" width="4" height="4"/><rect x="12" y="12" width="4" height="4"/></svg>
    <svg width="18" height="16" viewBox="0 0 18 16" fill="#9a9a9a"><rect x="0" y="1" width="3" height="2"/><rect x="5" y="1" width="13" height="2"/><rect x="0" y="7" width="3" height="2"/><rect x="5" y="7" width="13" height="2"/><rect x="0" y="13" width="3" height="2"/><rect x="5" y="13" width="13" height="2"/></svg>
  </div>
  Showing 1–16 Of 21 Results
  <div class="sort">Sort By : <div class="select">Relevance <svg width="9" height="6" viewBox="0 0 9 6" fill="none" stroke="#999"><path d="M1 1l3.5 3.5L8 1"/></svg></div></div>
</div>

<main class="grid">
  <article class="card"><div class="photo" role="img" aria-label="Stainless slow cooker" style="background:radial-gradient(circle,#bdbdbd,#f4f4f4 75%)"></div><h3>Calvera 30 Pieces<br>Dinnerware Set</h3><p class="price">Price: <b>$86.00</b></p><p class="stars">★★★★★</p><div class="actions"><span class="wish"><svg width="14" height="12" viewBox="0 0 30 26" fill="#666"><path d="M15 24S2 16 2 8a6.5 6.5 0 0113-1 6.5 6.5 0 0113 1c0 8-13 16-13 16z"/></svg></span><a class="cart">ADD TO CART</a></div></article>
  <article class="card"><div class="photo" role="img" aria-label="Chrome dish drying rack" style="background:radial-gradient(circle,#cfcfcf,#f6f6f6 75%)"></div><h3>Calvera 30 Pieces<br>Dinnerware Set</h3><p class="price">Price: <b>$86.00</b></p><p class="stars">★★★★★</p><div class="actions"><span class="wish"><svg width="14" height="12" viewBox="0 0 30 26" fill="#666"><path d="M15 24S2 16 2 8a6.5 6.5 0 0113-1 6.5 6.5 0 0113 1c0 8-13 16-13 16z"/></svg></span><a class="cart">ADD TO CART</a></div></article>
  <article class="card"><div class="photo" role="img" aria-label="Steel camping cookware set" style="background:radial-gradient(circle,#b5b5b5,#f4f4f4 75%)"></div><h3>Calvera 30 Pieces<br>Dinnerware Set</h3><p class="price">Price: <b>$86.00</b></p><p class="stars">★★★★★</p><div class="actions"><span class="wish"><svg width="14" height="12" viewBox="0 0 30 26" fill="#666"><path d="M15 24S2 16 2 8a6.5 6.5 0 0113-1 6.5 6.5 0 0113 1c0 8-13 16-13 16z"/></svg></span><a class="cart">ADD TO CART</a></div></article>
  <article class="card"><div class="photo" role="img" aria-label="Pot and pan set with glass lids" style="background:radial-gradient(circle,#bcbcbc,#f4f4f4 75%)"></div><h3>Calvera 30 Pieces<br>Dinnerware Set</h3><p class="price">Price: <b>$86.00</b></p><p class="stars">★★★★★</p><div class="actions"><span class="wish"><svg width="14" height="12" viewBox="0 0 30 26" fill="#666"><path d="M15 24S2 16 2 8a6.5 6.5 0 0113-1 6.5 6.5 0 0113 1c0 8-13 16-13 16z"/></svg></span><a class="cart">ADD TO CART</a></div></article>
  <article class="card"><div class="photo" role="img" aria-label="Stainless stock pot set" style="background:radial-gradient(circle,#c2c2c2,#f6f6f6 75%)"></div><h3>Calvera 30 Pieces<br>Dinnerware Set</h3><p class="price">Price: <b>$86.00</b></p><p class="stars">★★★★★</p><div class="actions"><span class="wish"><svg width="14" height="12" viewBox="0 0 30 26" fill="#666"><path d="M15 24S2 16 2 8a6.5 6.5 0 0113-1 6.5 6.5 0 0113 1c0 8-13 16-13 16z"/></svg></span><a class="cart">ADD TO CART</a></div></article>
  <article class="card"><div class="photo" role="img" aria-label="Round steel serving tray" style="background:radial-gradient(ellipse,#c8c8c8,#f6f6f6 70%)"></div><h3>Calvera 30 Pieces<br>Dinnerware Set</h3><p class="price">Price: <b>$86.00</b></p><p class="stars">★★★★★</p><div class="actions"><span class="wish"><svg width="14" height="12" viewBox="0 0 30 26" fill="#666"><path d="M15 24S2 16 2 8a6.5 6.5 0 0113-1 6.5 6.5 0 0113 1c0 8-13 16-13 16z"/></svg></span><a class="cart">ADD TO CART</a></div></article>
  <article class="card"><div class="photo" role="img" aria-label="Steel serving bowl" style="background:radial-gradient(ellipse,#c6c6c6,#f6f6f6 70%)"></div><h3>Calvera 30 Pieces<br>Dinnerware Set</h3><p class="price">Price: <b>$86.00</b></p><p class="stars">★★★★★</p><div class="actions"><span class="wish"><svg width="14" height="12" viewBox="0 0 30 26" fill="#666"><path d="M15 24S2 16 2 8a6.5 6.5 0 0113-1 6.5 6.5 0 0113 1c0 8-13 16-13 16z"/></svg></span><a class="cart">ADD TO CART</a></div></article>
  <article class="card"><div class="photo" role="img" aria-label="Stacked steel plates, cups and spoons" style="background:radial-gradient(circle,#b0b0b0,#f4f4f4 75%)"></div><h3>Calvera 30 Pieces<br>Dinnerware Set</h3><p class="price">Price: <b>$86.00</b></p><p class="stars">★★★★★</p><div class="actions"><span class="wish"><svg width="14" height="12" viewBox="0 0 30 26" fill="#666"><path d="M15 24S2 16 2 8a6.5 6.5 0 0113-1 6.5 6.5 0 0113 1c0 8-13 16-13 16z"/></svg></span><a class="cart">ADD TO CART</a></div></article>
  <article class="card"><div class="photo" role="img" aria-label="Travel cutlery set with pouch" style="background:radial-gradient(circle,#c4c4c4,#f6f6f6 75%)"></div><h3>Calvera 30 Pieces<br>Dinnerware Set</h3><p class="price">Price: <b>$86.00</b></p><p class="stars">★★★★★</p><div class="actions"><span class="wish"><svg width="14" height="12" viewBox="0 0 30 26" fill="#666"><path d="M15 24S2 16 2 8a6.5 6.5 0 0113-1 6.5 6.5 0 0113 1c0 8-13 16-13 16z"/></svg></span><a class="cart">ADD TO CART</a></div></article>
  <article class="card"><div class="photo" role="img" aria-label="Small steel saucepan with long handle" style="background:radial-gradient(circle,#c8c8c8,#f6f6f6 70%)"></div><h3>Calvera 30 Pieces<br>Dinnerware Set</h3><p class="price">Price: <b>$86.00</b></p><p class="stars">★★★★★</p><div class="actions"><span class="wish"><svg width="14" height="12" viewBox="0 0 30 26" fill="#666"><path d="M15 24S2 16 2 8a6.5 6.5 0 0113-1 6.5 6.5 0 0113 1c0 8-13 16-13 16z"/></svg></span><a class="cart">ADD TO CART</a></div></article>
  <article class="card"><div class="photo" role="img" aria-label="Wire storage basket" style="background:radial-gradient(circle,#bababa,#f6f6f6 75%)"></div><h3>Calvera 30 Pieces<br>Dinnerware Set</h3><p class="price">Price: <b>$86.00</b></p><p class="stars">★★★★★</p><div class="actions"><span class="wish"><svg width="14" height="12" viewBox="0 0 30 26" fill="#666"><path d="M15 24S2 16 2 8a6.5 6.5 0 0113-1 6.5 6.5 0 0113 1c0 8-13 16-13 16z"/></svg></span><a class="cart">ADD TO CART</a></div></article>
  <article class="card"><div class="photo" role="img" aria-label="Divided steel meal plate" style="background:radial-gradient(circle,#9c9c9c,#ededed 75%)"></div><h3>Calvera 30 Pieces<br>Dinnerware Set</h3><p class="price">Price: <b>$86.00</b></p><p class="stars">★★★★★</p><div class="actions"><span class="wish"><svg width="14" height="12" viewBox="0 0 30 26" fill="#666"><path d="M15 24S2 16 2 8a6.5 6.5 0 0113-1 6.5 6.5 0 0113 1c0 8-13 16-13 16z"/></svg></span><a class="cart">ADD TO CART</a></div></article>
</main>

<nav class="pager">
  <a class="prev">‹&nbsp; Prev</a>
  <a class="num">1</a><a class="current">2</a><a class="num">3</a><span class="num">...</span><a class="num">82</a>
  <a class="next">Next &nbsp;›</a>
</nav>

<footer class="site-footer">
  <div class="footer-brand">
    <div class="name"><span></span>OWLBRASS</div>
    <p>Lorem ipsum dolor sit amet, consectetur adipisicing elit, sed do eiusmod .</p>
  </div>
  <div class="col" style="left:409px"><h4>INFORMATION</h4><ul><li>My Account</li><li>Wishlist</li><li>About Us</li><li>Contact Us</li><li>Blog</li></ul></div>
  <div class="col" style="left:619px"><h4>QUICK LINKS</h4><ul><li>Shipping policy</li><li>Size Chart</li><li>Login</li><li>My Account</li><li>Register</li></ul></div>
  <div class="col contact" style="left:846px;width:260px"><h4>CONTACT US</h4>
    <ul>
      <li><svg width="10" height="14" viewBox="0 0 10 14" fill="#fff" style="margin-top:3px;flex:none"><path d="M5 0a5 5 0 015 5c0 4-5 9-5 9S0 9 0 5a5 5 0 015-5z"/><circle cx="5" cy="5" r="2" fill="#40608e"/></svg>Your current address goes to here,120 example, country.</li>
      <li><svg width="12" height="12" viewBox="0 0 12 12" fill="#fff" style="margin-top:4px;flex:none"><path d="M2 0l3 3-1.5 2A7 7 0 007 8.5L9 7l3 3-2 2C5 12 0 7 0 2z"/></svg>(008) 254 254 254 25487</li>
      <li><svg width="12" height="10" viewBox="0 0 12 10" fill="#fff" style="margin-top:5px;flex:none"><rect width="12" height="10"/><path d="M0 0l6 5 6-5" stroke="#40608e" fill="none"/></svg>example@admin.com</li>
    </ul>
    <div class="social"><span></span><span></span><span></span><span></span><span></span><span></span></div>
  </div>
  <div class="footer-rule"></div>
  <div class="copyright">© 2020 Owlbrass | All Rights Reserved.</div>
  <div class="legal">PRIVACY POLICY - TERMS OF USE</div>
  <a class="to-top"><svg width="10" height="7" viewBox="0 0 10 7" fill="none" stroke="#333" stroke-width="1.6"><path d="M1 6l4-4 4 4"/></svg></a>
</footer>

</body>
</html>
```